Calm Fern Healthcare- Aged Care and Community Services

Looking for brochure to advertise our services. I will attach a draft that we do not want to use. Looking for graphics that are as natural as possible to present a personalised service. We supply services to aged people and people with disability. Please make it look classy and professional at the same time. I am looking for creativity. I have also attached the logo. Site addresses can be the last page. ideally looking for 2 designs, one A4 and another smaller possibly DL. Looking for creative out of the box thinkers. Thank you.

Target Market(s)

Aged Care service providers, disability service providers and private hospitals

Font styles to use
Serif
Sans Serif
Script

Colors
6b449b
886aae
eea4c8
f59195
fac994
3176b5
0555a3
cedeed
e4daeb

Requirements
Must have
• Targeted imagery, content and contact details
Nice to have
• personal profiles of people happy with our services

```html
<!DOCTYPE html>
<html lang="en">
<head>
<meta charset="utf-8">
<title>Calm Fern Healthcare – Brochure</title>
<link href="https://fonts.googleapis.com/css2?family=Montserrat:wght@300;400;500;600&display=swap" rel="stylesheet">
<style>
  :root{
    --bg:#5e5e5e;
    --paper:#f7f6fa;
    --purple:#6b449b;
    --lilac:#886aae;
    --magenta:#c8338f;
    --pink:#c671b1;
    --ink:#2b2b33;
    --muted:#55535e;
  }
  *{box-sizing:border-box;margin:0;padding:0}
  html,body{width:1200px;height:789px;overflow:hidden}
  body{background:var(--bg);font-family:'Montserrat',sans-serif;color:var(--ink)}
  .spread{position:absolute;left:77px;top:24px;width:1046px;height:740px;display:flex;box-shadow:0 10px 30px rgba(0,0,0,.35)}
  .page{position:relative;width:523px;height:740px;background:var(--paper);overflow:hidden}
  .page--back{background:linear-gradient(90deg,#f4f3f8 0%,#eceaf1 100%)}
  .page-band{position:absolute;left:0;right:0;bottom:0;height:10px;background:linear-gradient(90deg,var(--purple),var(--magenta))}
  .dot{position:absolute;border-radius:50%}
  .photo{position:absolute;border-radius:50%}
  .ring{position:absolute;border-radius:50%;border:1px solid var(--purple)}
  .heading{position:absolute;font-weight:400;font-size:24px;color:var(--ink)}
  .heading span{color:var(--magenta)}
  .rule{position:absolute;height:1px;background:var(--magenta)}
  .about-text{position:absolute;left:40px;top:362px;width:285px;font-size:7.6px;line-height:1.55;color:var(--muted)}
  .about-text p+p{margin-top:10px}
  .brand-mark{position:absolute;display:flex;align-items:center;gap:6px;font-weight:500;color:var(--purple);white-space:nowrap}
  .brand-mark i{display:block;border-radius:50%;background:var(--purple)}
  .contact-list{position:absolute;left:40px;top:548px;width:250px;font-size:9px;line-height:1.45;color:var(--muted)}
  .contact-item{position:relative;padding-left:14px;margin-bottom:12px}
  .contact-item h4{font-size:10px;font-weight:600;color:var(--purple);letter-spacing:.3px}
  .contact-item .detail{border-left:1.5px solid var(--magenta);padding-left:8px;margin-left:-6px}
  .contact-item svg{position:absolute;left:0;top:1px}
  .contact-line{display:flex;align-items:center;gap:6px;margin-bottom:3px}
  .hours{position:absolute;left:300px;top:508px;width:200px;font-size:8.5px;line-height:1.45;color:var(--muted)}
  .hours h4{display:flex;align-items:center;gap:6px;font-size:10px;font-weight:600;color:var(--purple);margin-bottom:22px}
  .hours .slot{border-left:1.5px solid var(--magenta);padding-left:8px;margin-bottom:12px}
  .hours .slot em{font-style:normal;color:var(--magenta)}
  .social{position:absolute;left:370px;top:640px;display:flex;gap:8px}
  .social span{width:18px;height:18px;border-radius:50%;background:var(--purple)}
  .cover-brand{position:absolute;left:0;right:0;top:48px;display:flex;justify-content:center}
  .tagline{position:absolute;right:40px;top:500px;text-align:right}
  .tagline .line1{font-size:54px;font-weight:300;letter-spacing:1px;color:#111;line-height:1}
  .tagline .line2{display:inline-block;margin-top:8px;background:var(--magenta);color:#fff;font-size:48px;font-weight:300;padding:4px 22px 6px 40px;line-height:1.05}
  .cover-web{position:absolute;left:0;right:0;top:660px;text-align:center;font-size:10px;letter-spacing:2.5px;color:var(--muted)}
  .cover-web b{color:var(--purple);font-weight:600}
</style>
</head>
<body>
<main class="spread">

  <section class="page page--back">
    <div class="dot" style="left:-80px;top:40px;width:230px;height:230px;background:var(--pink);opacity:.85"></div>
    <div class="ring" style="left:120px;top:5px;width:262px;height:262px"></div>
    <div class="photo" role="img" aria-label="Photo of a carer giving an elderly woman a high five outdoors" style="left:128px;top:13px;width:246px;height:246px;background:linear-gradient(150deg,#9cc47a 0%,#6f9a58 45%,#d9d3c8 75%,#8fb2d8 100%)"></div>
    <div class="dot" style="left:192px;top:232px;width:76px;height:76px;background:var(--lilac);opacity:.9"></div>

    <h2 class="heading" style="left:40px;top:318px">About <span>Us</span></h2>
    <div class="rule" style="left:40px;top:352px;width:270px"></div>
    <div class="about-text">
      <p>Calm Fern Healthcare is a staffing provider with a contemporary approach to recruiting and placing exceptional people in human services. We maintain a comprehensive database of General Registered Nurses, Enrolled Nurses, Nursing Assistants, Medication Competent Nursing Assistants, Chefs, Cooks, Catering Assistants, Kitchen hands, Laundry and Cleaning staff. Our staff are skilled in Aged Care, Disability Services, Community Care, Public and Private Healthcare.</p>
      <p>Our vision is to be the most responsive staffing agency in Australia.</p>
    </div>

    <div class="brand-mark" style="left:352px;top:392px;font-size:11px"><i style="width:12px;height:12px"></i>Calm Fern Healthcare</div>
    <div class="rule" style="left:300px;top:438px;width:190px"></div>

    <h2 class="heading" style="left:40px;top:494px">Contact <span>Us</span></h2>
    <div class="rule" style="left:40px;top:528px;width:440px"></div>

    <div class="contact-list">
      <div class="contact-item">
        <svg width="9" height="11" viewBox="0 0 9 11"><path d="M4.5 0.5a3.5 3.5 0 0 1 3.5 3.5c0 2.6-3.5 6.5-3.5 6.5S1 6.6 1 4a3.5 3.5 0 0 1 3.5-3.5z" fill="var(--magenta)"/><circle cx="4.5" cy="4" r="1.3" fill="#fff"/></svg>
        <h4>PERTH</h4>
        <div class="detail">18 Wattle Road<br>Fernvale WA 6999</div>
      </div>
      <div class="contact-item">
        <svg width="9" height="11" viewBox="0 0 9 11"><path d="M4.5 0.5a3.5 3.5 0 0 1 3.5 3.5c0 2.6-3.5 6.5-3.5 6.5S1 6.6 1 4a3.5 3.5 0 0 1 3.5-3.5z" fill="var(--magenta)"/><circle cx="4.5" cy="4" r="1.3" fill="#fff"/></svg>
        <h4>ADELAIDE</h4>
        <div class="detail">Ground Floor, 12 Harbour Street,<br>Lakeview SA 5999</div>
      </div>
      <div class="contact-line">
        <svg width="9" height="7" viewBox="0 0 9 7"><rect x=".5" y=".5" width="8" height="6" fill="none" stroke="var(--magenta)"/><path d="M.5.5l4 3 4-3" fill="none" stroke="var(--magenta)"/></svg>
        admin@calmfernhealthcare.com.au
      </div>
      <div class="contact-line">
        <svg width="9" height="9" viewBox="0 0 9 9"><circle cx="4.5" cy="4.5" r="4" fill="none" stroke="var(--magenta)"/><path d="M3 2.5l1 1-.6.8c.4.8.9 1.3 1.7 1.7l.8-.6 1 1-.8.9C4.5 7 2 4.5 2.2 3.2z" fill="var(--magenta)"/></svg>
        08 9000 1234
      </div>
      <div class="contact-line">
        <svg width="9" height="9" viewBox="0 0 9 9"><circle cx="4.5" cy="4.5" r="4" fill="var(--magenta)"/><path d="M.5 4.5h8M4.5.5c-2 2.5-2 5.5 0 8M4.5.5c2 2.5 2 5.5 0 8" fill="none" stroke="#fff" stroke-width=".6"/></svg>
        www.calmfernhealthcare.com.au
      </div>
    </div>

    <div class="hours">
      <h4><svg width="10" height="10" viewBox="0 0 10 10"><rect x=".5" y="1.5" width="9" height="8" fill="none" stroke="var(--magenta)"/><path d="M.5 4h9M3 .5v2M7 .5v2" stroke="var(--magenta)"/></svg>OFFICE HOURS</h4>
      <div class="slot"><em>Monday to Friday</em> 9am–5pm<br>Afterhours (Bookings Only)</div>
      <div class="slot"><em>Monday–Friday</em> 5pm–10pm/ 6am–9am;<br>Saturdays and Sunday (all hours)</div>
    </div>

    <div class="social" aria-label="Social media links"><span></span><span></span><span></span></div>

    <div class="page-band"></div>
  </section>

  <section class="page page--cover">
    <div class="cover-brand">
      <div class="brand-mark" style="position:static;font-size:17px"><i style="width:16px;height:16px"></i>Calm Fern Healthcare</div>
    </div>

    <div class="dot" style="left:360px;top:80px;width:64px;height:64px;background:var(--pink);opacity:.85"></div>
    <div class="dot" style="left:92px;top:152px;width:34px;height:34px;background:var(--lilac);opacity:.8"></div>

    <div class="ring" style="left:22px;top:150px;width:216px;height:216px"></div>
    <div class="photo" role="img" aria-label="Photo of a smiling group of elderly friends outdoors" style="left:28px;top:156px;width:204px;height:204px;background:linear-gradient(160deg,#a8c98a 0%,#7fa76a 40%,#e8e4de 70%,#c7c2bb 100%)"></div>

    <div class="ring" style="left:212px;top:102px;width:290px;height:290px"></div>
    <div class="photo" role="img" aria-label="Photo of a laughing elderly woman with a nurse beside her" style="left:218px;top:108px;width:278px;height:278px;background:linear-gradient(140deg,#d2cfcd 0%,#f1ece8 40%,#e7c9d6 70%,#8fb8d9 100%)"></div>

    <div class="ring" style="left:138px;top:300px;width:168px;height:168px"></div>
    <div class="photo" role="img" aria-label="Photo of a carer helping an elderly man walk with a frame" style="left:144px;top:306px;width:156px;height:156px;background:linear-gradient(160deg,#cdb89a 0%,#e9e6e1 45%,#9ec3e2 80%,#7c8fa8 100%)"></div>

    <div class="dot" style="left:410px;top:330px;width:100px;height:100px;background:var(--lilac);opacity:.85"></div>
    <div class="dot" style="left:395px;top:430px;width:44px;height:44px;background:var(--pink);opacity:.85"></div>

    <div class="tagline">
      <div class="line1">BECAUSE</div>
      <div class="line2">WE CARE</div>
    </div>

    <div class="cover-web">www.<b>CalmFernHealthcare</b>.com.au</div>

    <div class="page-band"></div>
  </section>

</main>
</body>
</html>
```